Scandinavian film company needs new website

We need a new web design for our company based in Roskilde, Denmark called Solvik Film (translated: Dawn Film).

We are a creative company that make video content to social media and provides professional photographers and technicians for multi-camera productions.

We want a scroll-down site where everything is accessible on the same page. The individual elements of the page must be accessible by a menu bar at the top.

The design should be a wordpress template or the like, which we can edit and work with on our own after delivery.

The color scheme must be consistent with one of the attached logo designs - but are welcome to come up with complementary colors to match the logo colors. We prefer black/dark grey background over white.

We've attached some atmospheric photos from our workplaces and some equipment photos which can be used or be inspiration for background design.

Websites for inspiration:
http://tovaren.dk/
- inspired by color scheme and the simple structure of the website.

http://www.brimholtvarnesen.dk/
- inspired by background photos that does not move and simple structure of the website.

http://gomrup.dk/
- inspired by the simple structure of the website

http://www.kivaproductions.dk/
- inspired by the simple structure of the frontpage

The website should contain:

Profile
- Hvem er vi (english: Who we are)
- Hvorfor vælge os (english: why pick us)
- Sådan kommer du godt i gang (english: how do you get started)

Services
- Videoproduktion
- Animationsfilm
- Redigering (english: editing)
- OB-produktion

Portfolio (video gallery)

References (minimum 8 logos)

Follow us (Flimor / Clipwave / Boardly / Snapturo)

Contact

Target Market(s)

Communication and marketing departments in large and medium-sized Danish companies

Industry/Entity Type

Videography

Coding

Coded - Design and coding required

Number of Pages Required

1 page

Font styles to use
Sans Serif

Colors
000000
333333
3276b5
fbf289

Requirements
Must have
• - Logo
• - Responsive design (videos must look good on mobile devices)
• - Color scheme must be consistent with one of the attached logo designs - we prefer black/dark grey backgrounds.
• - The code/design should be a wordpress template or the like, which we can edit and work with on our own after delivery.
• Website should contain:
• Solvik Film
• - Hvem er vi (english: Who we are)
• - Hvorfor vælge os (english: why pick us)
• - Sådan kommer du godt i gang (english: how do you get started)
• Services
• - Videoproduktion
• - Animationsfilm
• - Redigering (english: editing)
• - OB-produktion
• Portfolio (video gallery)
• References (minimum 8 logos)
• Follow us (Flimor / Clipwave / Boardly / Snapturo)
• Contact
Should not have
• Contact formular
• Subpages
• Unnecessary elements

```html
<!DOCTYPE html>
<html lang="da">
<head>
<meta charset="utf-8">
<title>Solvik Film</title>
<link rel="stylesheet" href="https://fonts.googleapis.com/css2?family=Open+Sans:wght@300;400;600;700;800&display=swap">
<style>
:root{
  --teal:#17383f;
  --teal-dark:#0f2a30;
  --yellow:#ead56c;
  --yellow-soft:#f0dd7a;
  --charcoal:#3a3d40;
  --charcoal-dark:#2e3134;
  --paper:#f1f1f1;
  --card:#f6f3ec;
  --ink:#2b2b2b;
  --muted:#666;
  --white:#fff;
  --ref-bg:#ececec;
}
*{box-sizing:border-box;margin:0;padding:0}
html,body{width:1200px;height:2885px;overflow:hidden}
body{position:relative;font-family:"Open Sans",Arial,sans-serif;color:var(--ink);background:var(--white)}
.abs{position:absolute}

/* Header */
.site-header{position:absolute;left:0;top:0;width:1200px;height:165px;background:var(--white);border-bottom:1px solid #e3e3e3}
.brand{position:absolute;left:100px;top:40px;display:flex;align-items:center;gap:12px}
.brand-dot{width:48px;height:48px;border-radius:50%;background:var(--teal)}
.brand-name{font-size:30px;font-weight:600;color:var(--teal);letter-spacing:.5px}
.main-nav{position:absolute;top:64px;left:460px;display:flex;align-items:center;font-size:13px;font-weight:600;color:var(--teal)}
.main-nav a{color:inherit;text-decoration:none;display:block;padding:11px 12px;line-height:18px}
.main-nav a.active{background:var(--teal);color:var(--yellow)}
.nav-profile{margin-left:12px}
.nav-gap{margin-left:22px}
.search{position:absolute;left:1076px;top:72px}

/* Hero */
.hero{position:absolute;left:0;top:165px;width:1200px;height:515px;background:radial-gradient(ellipse at 55% 10%,#b6d1e0 0%,#6f8ea3 22%,#3a3b3d 55%,#1c1a19 100%)}
.hero-title{position:absolute;left:0;width:1200px;top:178px;text-align:center;font-size:74px;font-weight:800;color:var(--white);letter-spacing:1px;line-height:1}
.hero-sub{position:absolute;left:0;width:1200px;top:286px;text-align:center;font-size:30px;font-weight:700;color:var(--yellow);letter-spacing:1px}
.emblem{position:absolute;left:540px;top:620px;width:120px;height:120px;border-radius:50%;background:var(--charcoal);z-index:2}
.emblem-dot{position:absolute;left:30px;top:22px;width:60px;height:60px;border-radius:50%;background:var(--yellow)}

/* Profile */
.profile{position:absolute;left:0;top:680px;width:1200px;height:557px;background:var(--charcoal);
  background-image:repeating-linear-gradient(45deg,rgba(255,255,255,.03) 0 2px,transparent 2px 6px)}
.section-title{position:absolute;left:0;width:1200px;text-align:center;font-weight:400;font-size:34px}
.profile .section-title{top:48px;color:var(--white)}
.pcard{position:absolute;top:126px;width:314px;height:386px;background:var(--paper)}
.pcard-head{height:65px;display:flex;align-items:center;padding-left:38px;gap:12px;font-size:17px;font-weight:600;color:var(--white);background:var(--teal)}
.pcard-head.alt{background:var(--yellow);color:var(--teal)}
.pcard-body{padding:30px 24px 0;text-align:center}
.pcard-body h3{font-size:15px;font-weight:600;color:var(--ink);margin-bottom:14px;line-height:20px}
.pcard-body p{font-size:11.5px;line-height:20px;color:#555}
.more{position:absolute;left:0;width:100%;text-align:center;font-size:13px;font-weight:700;color:var(--ink);letter-spacing:.3px}
.btn{position:absolute;left:100px;width:120px;height:46px;background:var(--teal);color:var(--white);font-size:12px;font-weight:600;display:flex;align-items:center;justify-content:center}

/* Services */
.services{position:absolute;left:0;top:1237px;width:1200px;height:473px;background:var(--white)}
.services .section-title{top:50px;color:var(--teal)}
.services-sub{position:absolute;left:0;width:1200px;top:102px;text-align:center;font-size:17px;color:#555}
.scard{position:absolute;top:205px;width:316px;height:196px;background:var(--card);text-align:center}
.scard-icon{position:absolute;left:116px;top:-41px;width:84px;height:84px;border-radius:50%;background:var(--charcoal-dark);display:flex;align-items:center;justify-content:center}
.scard-icon.alt{background:var(--yellow)}
.scard h3{position:absolute;top:66px;width:100%;font-size:15px;font-weight:600;color:var(--ink)}
.scard h3.teal{color:var(--teal)}
.scard p{position:absolute;top:96px;left:30px;width:256px;font-size:12px;line-height:19px;color:#666}
.scard .rule{position:absolute;left:30px;right:30px;top:150px;border-top:1px solid #e4e0d6}
.scard .scard-more{position:absolute;top:163px;width:100%;font-size:11px;font-weight:600;color:var(--teal)}

/* Portfolio */
.portfolio{position:absolute;left:0;top:1710px;width:1200px;height:612px;background:linear-gradient(135deg,#3a3a38 0%,#5b5247 40%,#2e2b29 70%,#463d33 100%)}
.portfolio .section-title{top:28px;color:var(--white)}
.video{position:absolute;width:314px;height:215px;border:1px solid #666;overflow:hidden}
.video-frame{position:absolute;left:0;top:0;width:100%;height:191px}
.video-bar{position:absolute;left:0;bottom:0;width:100%;height:24px;background:#161616}
.play{position:absolute;left:128px;top:66px}

/* References */
.references{position:absolute;left:0;top:2322px;width:1200px;height:323px;background:var(--ref-bg)}
.references .section-title{top:44px;color:var(--teal)}
.dots{position:absolute;left:578px;top:110px;display:flex;gap:6px}
.dots i{width:9px;height:9px;border-radius:50%;background:#ccc;display:block}
.dots i.on{background:var(--white);border:2px solid #8aa}
.ref{position:absolute;top:158px;width:192px;height:103px;background:var(--white);display:flex;align-items:center;justify-content:center;font-size:17px;font-weight:700;color:#444;text-align:center}

/* Footer */
.site-footer{position:absolute;left:0;top:2645px;width:1200px;height:205px;background:var(--charcoal)}
.foot-brand{position:absolute;left:180px;top:80px;display:flex;align-items:center;gap:10px}
.foot-brand .brand-dot{background:var(--yellow);width:40px;height:40px}
.foot-brand .brand-name{color:var(--yellow);font-size:28px}
.foot-col h4{font-size:15px;font-weight:700;color:var(--white)}
.foot-line{position:absolute;font-size:12px;color:#ddd;display:flex;align-items:center;gap:12px}
.social{position:absolute;left:846px;top:90px;display:flex;gap:14px}
.social span{display:flex;align-items:center;gap:5px;font-size:11px;color:#ccc}
.social span i{width:16px;height:16px;border-radius:50%;background:#6a7075;display:block}
.copyright{position:absolute;left:0;top:2850px;width:1200px;height:35px;background:var(--yellow);text-align:center;font-size:12px;font-weight:600;color:var(--ink);line-height:35px}
</style>
</head>
<body>

<header class="site-header">
  <div class="brand"><span class="brand-dot"></span><span class="brand-name">Solvik Film</span></div>
  <nav class="main-nav">
    <a class="active" href="#">Home</a>
    <a class="nav-profile" href="#profile">Profile</a>
    <a class="nav-gap" href="#services">Services</a>
    <a class="nav-gap" href="#portfolio">Portfolio</a>
    <a class="nav-gap" href="#references">References</a>
    <a class="nav-gap" href="#contact">Contact / follow us</a>
  </nav>
  <svg class="search" width="24" height="24" viewBox="0 0 24 24"><circle cx="10" cy="10" r="7" fill="none" stroke="#17383f" stroke-width="3"/><line x1="15" y1="15" x2="21" y2="21" stroke="#17383f" stroke-width="3.5" stroke-linecap="round"/></svg>
</header>

<section class="hero" role="img" aria-label="Concert crowd with raised hands under bright stage lights">
  <h1 class="hero-title">WELCOME TO</h1>
  <p class="hero-sub">SOLVIK FILM</p>
</section>
<div class="emblem"><span class="emblem-dot"></span></div>

<section class="profile" id="profile">
  <h2 class="section-title">Profile</h2>

  <article class="pcard" style="left:100px">
    <div class="pcard-head">
      <svg width="32" height="32" viewBox="0 0 32 32"><rect width="32" height="32" rx="3" fill="#fff"/><text x="16" y="25" text-anchor="middle" font-family="Open Sans,sans-serif" font-size="24" font-weight="800" fill="#17383f">?</text></svg>
      How can we help you?
    </div>
    <div class="pcard-body">
      <h3>Solvik Film Hvem er vi?</h3>
      <p>Solvik Film leverer videoproduktioner og videofotografer til små og store danske virksomheder og organisationer. Vi tager hånd om alle faser i en videoproduktion – fra idé til færdig film, så det eneste du skal gøre, er at være åben omkring dine ønsker og behov. Hos os kan du få produceret reklamefilm, animationsfilm, præsentationsfilm.</p>
    </div>
    <div class="more" style="top:338px">READ MORE &nbsp;➜</div>
  </article>

  <article class="pcard" style="left:443px">
    <div class="pcard-head alt">
      <svg width="28" height="30" viewBox="0 0 28 30"><rect x="4" y="2" width="20" height="26" rx="3" fill="#17383f"/><rect x="9" y="8" width="10" height="3" fill="#ead56c"/><rect x="9" y="15" width="10" height="3" fill="#ead56c"/></svg>
      Why pick us?
    </div>
    <div class="pcard-body">
      <h3>HVORFOR &nbsp;VÆLGE OS?</h3>
      <p>Din vision er vores mission. Vi er ikke stødt på en opgave vi ikke kunne klare. Når du som klient bliver sat op til et uforpligtigende introduktionsmøde med os, bliver du vejledt bedst muligt gennem projektet. Vi er stolte over at vi allerede leverer video til disse virksomheder: Hjælpekorset, Aksel Brink Koncertsal, Nordvig Pharma, Kastrup Rådgivning.</p>
    </div>
    <div class="more" style="top:346px">READ MORE &nbsp;➜</div>
  </article>

  <article class="pcard" style="left:786px">
    <div class="pcard-head">
      <svg width="30" height="30" viewBox="0 0 30 30"><circle cx="15" cy="15" r="14" fill="#fff"/><circle cx="15" cy="9" r="2.3" fill="#17383f"/><rect x="13" y="13" width="4" height="10" fill="#17383f"/></svg>
      How do you get started?
    </div>
    <div class="pcard-body">
      <h3>HVORDAN KOMMER DU GODT<br>I GANG?</h3>
      <p>Vores erfaring viser, at jo tidligere vi bliver inkluderet i dine overvejelser om at lave en film jo bedre bliver forløbet og resultatet. Få uforpligtende sparring på dine idéer så du undgår faldgruber og udnytter det potentiale der er i at vælge den rigtige løsning fra starten. Kontakt os eller bliv ringet op:</p>
    </div>
    <div class="btn" style="top:314px">GET STARTED</div>
  </article>
</section>

<section class="services" id="services">
  <h2 class="section-title">Services</h2>
  <p class="services-sub">professional photographers and technicians for multi-camera productions .</p>

  <article class="scard" style="left:100px">
    <div class="scard-icon"><svg width="40" height="30" viewBox="0 0 40 30"><rect x="2" y="7" width="36" height="22" rx="3" fill="#fff"/><rect x="13" y="2" width="14" height="7" fill="#fff"/><circle cx="20" cy="18" r="7" fill="#2e3134"/><circle cx="20" cy="18" r="4" fill="#fff"/></svg></div>
    <h3>PROFESSIONAL PHOTOGRAPHERS</h3>
    <p>Vestibulum purus quam, scelerisque ut, mollis sed, nonummy id, metus. Nullam a</p>
    <div class="rule"></div>
    <div class="scard-more">READ MORE &nbsp;↘</div>
  </article>

  <article class="scard" style="left:448px">
    <div class="scard-icon alt"><svg width="36" height="34" viewBox="0 0 36 34"><path d="M5 20 a13 13 0 0 1 26 0" fill="none" stroke="#17383f" stroke-width="4"/><rect x="2" y="18" width="8" height="13" rx="2" fill="#17383f"/><rect x="26" y="18" width="8" height="13" rx="2" fill="#17383f"/></svg></div>
    <h3 class="teal">TECHNICIANS FOR MULTI-CAMERA</h3>
    <p>Vestibulum purus quam, scelerisque ut, mollis sed, nonummy id, metus. Nullam a</p>
    <div class="rule"></div>
    <div class="scard-more">READ MORE &nbsp;↘</div>
  </article>

  <article class="scard" style="left:785px">
    <div class="scard-icon"><svg width="30" height="38" viewBox="0 0 30 38"><rect x="2" y="1" width="26" height="36" fill="#fff"/><g fill="#2e3134"><rect x="4" y="4" width="3" height="4"/><rect x="4" y="12" width="3" height="4"/><rect x="4" y="20" width="3" height="4"/><rect x="4" y="28" width="3" height="4"/><rect x="23" y="4" width="3" height="4"/><rect x="23" y="12" width="3" height="4"/><rect x="23" y="20" width="3" height="4"/><rect x="23" y="28" width="3" height="4"/><rect x="10" y="4" width="10" height="13"/><rect x="10" y="20" width="10" height="13"/></g></svg></div>
    <h3 class="teal">TECHNICIANS FOR MULTI-CAMERA</h3>
    <p>Vestibulum purus quam, scelerisque ut, mollis sed, nonummy id, metus. Nullam a</p>
    <div class="rule"></div>
    <div class="scard-more">READ MORE &nbsp;↘</div>
  </article>
</section>

<section class="portfolio" id="portfolio" role="img" aria-label="Blurred festival crowd as section background">
  <h2 class="section-title">Portfolio</h2>

  <div class="video" style="left:100px;top:94px"><div class="video-frame" role="img" aria-label="Video still: young woman with headphones dancing" style="background:linear-gradient(135deg,#7a7a78,#3c3c3c)"></div><div class="video-bar"></div>
    <svg class="play" width="56" height="56" viewBox="0 0 56 56"><circle cx="28" cy="28" r="26" fill="rgba(255,255,255,.15)" stroke="#fff" stroke-width="2"/><path d="M23 18 L38 28 L23 38Z" fill="#fff"/></svg></div>
  <div class="video" style="left:443px;top:94px"><div class="video-frame" role="img" aria-label="Video still: guitarist on stage in blue light" style="background:linear-gradient(135deg,#0e4f78,#4aa3d6 55%,#0c2b44)"></div><div class="video-bar"></div>
    <svg class="play" width="56" height="56" viewBox="0 0 56 56"><circle cx="28" cy="28" r="26" fill="rgba(255,255,255,.15)" stroke="#fff" stroke-width="2"/><path d="M23 18 L38 28 L23 38Z" fill="#fff"/></svg></div>
  <div class="video" style="left:786px;top:94px"><div class="video-frame" role="img" aria-label="Video still: woman with a vintage film camera" style="background:linear-gradient(135deg,#c9c4bb,#8a7d70)"></div><div class="video-bar"></div>
    <svg class="play" width="56" height="56" viewBox="0 0 56 56"><circle cx="28" cy="28" r="26" fill="rgba(255,255,255,.15)" stroke="#fff" stroke-width="2"/><path d="M23 18 L38 28 L23 38Z" fill="#fff"/></svg></div>
  <div class="video" style="left:100px;top:342px"><div class="video-frame" role="img" aria-label="Video still: festival audience outdoors" style="background:linear-gradient(180deg,#e4ebf0,#9a7b67)"></div><div class="video-bar"></div>
    <svg class="play" width="56" height="56" viewBox="0 0 56 56"><circle cx="28" cy="28" r="26" fill="rgba(255,255,255,.15)" stroke="#fff" stroke-width="2"/><path d="M23 18 L38 28 L23 38Z" fill="#fff"/></svg></div>
  <div class="video" style="left:443px;top:342px"><div class="video-frame" role="img" aria-label="Video still: photographer in a field" style="background:linear-gradient(180deg,#ece3c8,#b79a62)"></div><div class="video-bar"></div>
    <svg class="play" width="56" height="56" viewBox="0 0 56 56"><circle cx="28" cy="28" r="26" fill="rgba(255,255,255,.15)" stroke="#fff" stroke-width="2"/><path d="M23 18 L38 28 L23 38Z" fill="#fff"/></svg></div>
  <div class="video" style="left:786px;top:342px"><div class="video-frame" role="img" aria-label="Video still: runner at sunset" style="background:radial-gradient(circle at 40% 40%,#ffd27a,#d3641c 45%,#3b1a0c)"></div><div class="video-bar"></div>
    <svg class="play" width="56" height="56" viewBox="0 0 56 56"><circle cx="28" cy="28" r="26" fill="rgba(255,255,255,.15)" stroke="#fff" stroke-width="2"/><path d="M23 18 L38 28 L23 38Z" fill="#fff"/></svg></div>
</section>

<section class="references" id="references">
  <h2 class="section-title">References</h2>
  <div class="dots"><i></i><i></i><i class="on"></i></div>
  <div class="ref" style="left:102px">Halvmåne Bryg</div>
  <div class="ref" style="left:304px">Lovenor</div>
  <div class="ref" style="left:506px">Festhalle Nord</div>
  <div class="ref" style="left:706px">Aerovik Limited</div>
  <div class="ref" style="left:908px">Tevora Vision</div>
</section>

<footer class="site-footer" id="contact">
  <div class="foot-brand"><span class="brand-dot"></span><span class="brand-name">Solvik Film</span></div>
  <div class="foot-col abs" style="left:494px;top:30px"><h4>Contacts</h4></div>
  <div class="foot-line" style="left:494px;top:70px">
    <svg width="16" height="12" viewBox="0 0 16 12"><rect width="16" height="12" fill="#ead56c"/><path d="M0 0 L8 7 L16 0" fill="none" stroke="#3a3d40" stroke-width="1.5"/></svg>kontakt@solvikfilm.dk</div>
  <div class="foot-line" style="left:494px;top:99px">
    <svg width="16" height="16" viewBox="0 0 16 16"><path d="M3 1 L6 1 L7 5 L5 6.5 Q7 10 9.5 11 L11 9 L15 10 L15 13 Q14 15 11 15 Q2 12 1 4 Q1 2 3 1Z" fill="#ead56c"/></svg>+45 2078 5512</div>
  <div class="foot-line" style="left:494px;top:130px">Solvik Film - Roskilde - Danmark</div>
  <div class="foot-col abs" style="left:846px;top:30px"><h4>Stay Connected &nbsp;:</h4></div>
  <div class="social"><span><i></i>Frendly</span><span><i></i>Chirpo</span><span><i></i>Linkora</span><span><i></i>Gathero</span></div>
</footer>
<div class="copyright">Copyright @ 2015 . SolvikFilm &nbsp;| All Rights Reserved.</div>

</body>
</html>
```